Looking for a website homepage design

Hi, we are looking for a design for Homepage for our childcare centre
We want something really progressive, edgy, modern and premium. We want this website to standout but not cluttered. We only need a Homepage.
1366 Wx768 H
The call to action is join our community
We like the idea of a split screen
Divided into section
Locations and Enrolments
Tumble
Careers
Partnerships
We like angles and shapes, particularly triangles in the designs
Our company font is Hands of Sean
Have attached some designs that we like the look and feel of and some of our designs from our flyers and some images to use, you don't need to choose all the images, just whatever works with your design.
We have a STEM focus at our centres so something sciencey would be great.
Consider in the design will be viewed on desktop and mobile phones

Industry/Entity Type

childcare with Science focus

Number of Pages Required

1 page

Other font styles liked:
• hands of sean is our company font

Requirements
Must have
• Homepage for website
Nice to have
• Split screen design

```html
<!DOCTYPE html>
<html lang="en">
<head>
<meta charset="utf-8">
<title>Bright Sky Kindergarten</title>
<link href="https://fonts.googleapis.com/css2?family=Gochi+Hand&family=Lato:wght@400;700;900&display=swap" rel="stylesheet">
<style>
:root{
  --blue:#08a4e6;
  --navy:#1f6fc0;
  --orange:#f7941d;
  --red:#ef4136;
  --yellow:#d7d900;
  --lime:#e4e000;
  --green:#3db54a;
  --grass:#8cc63f;
  --tomato:#f05a28;
  --sun:#fff200;
  --ink:#444;
  --white:#fff;
}
*{margin:0;padding:0;box-sizing:border-box}
html,body{width:1200px;height:3928px;overflow:hidden;background:var(--white)}
body{position:relative;font-family:"Lato",sans-serif;color:var(--ink)}
.abs{position:absolute}
.hand{font-family:"Gochi Hand",cursive;font-weight:400;text-transform:uppercase}
.btn{position:absolute;display:flex;align-items:center;justify-content:center;border-radius:40px;color:var(--white);font-weight:900;font-size:16px;text-transform:uppercase}
.btn-red{background:var(--red)}
.btn-yellow{background:var(--yellow)}

/* header */
.brand-box{left:143px;top:8px;width:121px;height:122px;background:var(--white);box-shadow:0 2px 6px rgba(0,0,0,.2);z-index:5;display:flex;align-items:center;justify-content:center;text-align:center;font-weight:900;font-size:18px;line-height:1.1;color:var(--red)}
.topbar-phone{left:741px;top:8px;display:flex;align-items:center;gap:8px;font-weight:700;font-size:16px;color:#222}
.waitlist{left:906px;top:8px;width:148px;height:33px;background:var(--orange);color:var(--white);font-weight:700;font-size:15px;display:flex;align-items:center;justify-content:center}
.navbar{left:335px;top:49px;width:865px;height:50px;background:var(--blue)}
.navbar .tip{position:absolute;left:0;top:0;width:112px;height:50px;background:var(--orange);clip-path:polygon(30px 0,100% 0,100% 100%,0 100%)}
.navbar ul{list-style:none}
.navbar li{position:absolute;top:16px;color:var(--white);font-weight:700;font-size:14px;text-transform:uppercase;white-space:nowrap}

/* hero */
.hero{left:0;top:99px;width:1200px;height:630px}
.hero-photo{position:absolute;inset:0;background:radial-gradient(circle at 62% 45%,#7aa8e0 0,#2c3f80 25%,#18203e 55%,#0c1024 100%);clip-path:polygon(0 0,100% 0,100% 432px,915px 630px,0 603px)}
.hero-tri{position:absolute;inset:0;background:var(--blue);clip-path:polygon(0 432px,610px 500px,0 603px)}
.hero h1{position:absolute;left:143px;top:90px;font-weight:900;font-size:64px;line-height:1.08;color:var(--white)}
.hero h1 span{color:var(--orange)}
.hero p{position:absolute;left:143px;top:253px;font-weight:700;font-size:28px;line-height:35px;color:var(--white)}
.dots span{position:absolute;left:1126px;width:14px;height:14px;border-radius:50%;background:var(--white)}

/* advantage */
.adv-art{left:140px;top:758px;width:440px;height:397px;background:linear-gradient(160deg,#fffbd0 0,#fff7a0 40%,#f4ee9a 75%,#e3f0c8 100%)}
.adv-title{left:595px;top:778px;font-size:50px;color:var(--blue);white-space:nowrap}
.adv-title span{color:var(--orange)}
.adv-title sup{font-size:24px;vertical-align:28px}
.adv-text{left:598px;top:858px;width:456px;font-size:15px;line-height:29px;text-align:justify;color:#555}

/* pillars */
.pillars{left:0;top:1223px;width:1200px;height:270px;display:flex}
.pillar{position:relative;width:240px;height:270px;color:var(--white);text-align:center}
.pillar .icon{position:absolute;left:73px;top:-22px;width:94px;height:94px;border-radius:50%;background:var(--white);border:5px solid currentColor}
.pillar .icon i{position:absolute;inset:14px;border-radius:50%}
.pillar h3{position:absolute;left:0;right:0;top:100px;font-weight:900;font-size:20px;color:var(--white)}
.pillar p{position:absolute;left:22px;right:22px;top:139px;font-size:13px;line-height:21px;color:var(--white)}
.pillar a{position:absolute;left:0;right:0;top:221px;font-weight:900;font-size:14px;text-decoration:underline;color:var(--white)}

/* gallery */
.section-title{left:0;width:1200px;text-align:center;font-size:50px}
.gallery{left:143px;top:1677px;width:914px;display:grid;grid-template-columns:repeat(3,297px);grid-template-rows:228px 227px;gap:12px 11px}

/* team */
.team{left:0;top:2329px;width:1200px;height:447px;background:var(--blue)}
.team-photo{position:absolute;left:422px;top:0;width:778px;height:447px;background:linear-gradient(120deg,#f3ede3 0,#e9d9c4 45%,#cfae8a 100%)}
.team-card{position:absolute;left:143px;top:55px;width:452px;height:338px;background:var(--lime);clip-path:polygon(0 0,383px 0,100% 100%,0 100%)}
.team-card h2{position:absolute;left:47px;top:40px;font-size:46px;color:var(--white)}
.team-card p{position:absolute;left:47px;top:103px;width:315px;font-size:13.5px;line-height:21px;color:var(--white);text-align:justify}

/* partners */
.partner{top:2966px;width:211px;height:107px;border:2px solid #cfcfcf;background:var(--white);display:flex;align-items:center;justify-content:center}
.partner.active{background:#dff3fb;border-color:#9fd8ef}
.arrow{top:2998px;width:44px;height:44px;border-radius:50%;border:2px solid #9a9a9a;display:flex;align-items:center;justify-content:center}

/* tour */
.tour{left:0;top:3167px;width:1200px;height:237px;background:var(--blue);clip-path:polygon(0 0,100% 0,100% 165px,910px 237px,0 170px)}
.tour h2{position:absolute;left:143px;top:30px;font-size:46px;color:var(--white)}
.tour p{position:absolute;left:146px;top:98px;font-size:18px;line-height:24px;color:var(--white)}

/* footer */
.foot-brand{left:440px;top:3510px;width:180px;text-align:center;font-weight:900;font-size:28px;line-height:1.1;color:var(--red)}
.foot-nav li{position:absolute;top:3539px;list-style:none;font-size:14px;color:#333;text-transform:uppercase;white-space:nowrap}
.contact{top:3677px;display:flex;align-items:center;gap:16px;font-size:18px;line-height:25px;color:#444}
.contact .circ{width:54px;height:54px;border-radius:50%;display:flex;align-items:center;justify-content:center}
.copy{left:0;top:3775px;width:1200px;text-align:center;font-size:14px;color:#333}
.social span{position:absolute;top:3840px;width:26px;height:26px;border-radius:50%;border:2px solid var(--green)}
.grass{left:0;top:3886px;width:1200px;height:42px;background:linear-gradient(180deg,var(--grass),var(--green))}
</style>
</head>
<body>

<header>
  <div class="abs brand-box">Bright Sky<br>Kinder&shy;garten</div>
  <div class="abs topbar-phone">
    <svg width="32" height="32" viewBox="0 0 32 32"><circle cx="16" cy="16" r="14" fill="none" stroke="#ef4136" stroke-width="3"/><path d="M11 9c1-1 2-1 3 0l1.5 2.5c.5 1 0 1.8-.6 2.3l-1 .8c.8 2 2.4 3.6 4.4 4.4l.8-1c.5-.6 1.3-1.1 2.3-.6L23 18.9c1 1 1 2 0 3-1.5 1.5-3.5 1.6-5.5.6-3-1.5-5.5-4-7-7-1-2-.9-4 .5-5.5z" fill="#ef4136"/></svg>
    (02) 9000 1234
  </div>
  <div class="abs waitlist">JOIN WAITLIST</div>
  <nav class="abs navbar">
    <div class="tip"></div>
    <ul>
      <li style="left:50px">Home</li>
      <li style="left:133px">About Us</li>
      <li style="left:229px">Gallery</li>
      <li style="left:316px">Sky Advantage™</li>
      <li style="left:484px">Locations</li>
      <li style="left:589px">Request A Tour</li>
    </ul>
  </nav>
</header>

<section class="abs hero">
  <div class="hero-photo" role="img" aria-label="Child's hand on a glowing plasma ball inside the Tumble STEM hub"></div>
  <div class="hero-tri"></div>
  <h1><span>BRIGHT SKY</span><br>KINDERGARTEN™</h1>
  <p>Presenting Tumble an industry<br>First,Pioneering,Stem Hub</p>
  <div class="btn btn-red" style="left:143px;top:352px;width:177px;height:63px">Get Started</div>
  <div class="dots"><span style="top:222px"></span><span style="top:249px;background:var(--blue)"></span><span style="top:277px"></span></div>
</section>

<section>
  <div class="abs adv-art" role="img" aria-label="Illustration of a smiling sun with a child flying a kite"></div>
  <h2 class="abs hand adv-title">The Sky <span>Advantage<sup>™</sup></span></h2>
  <p class="abs adv-text">Here at Bright Sky Kindergarten™ we have developed our own unique curriculum to ensure your child is learning and developing holistically; it's called the Sky Advantage™ program. We know that learning letters and numbers is important for your child, but it's only one small part of how they will grow and develop as a person. In order to promote the holistic development of your child, our curriculum consists of five key elements.</p>
  <div class="btn btn-red" style="left:598px;top:1086px;width:177px;height:61px">Read More</div>
</section>

<section class="abs pillars">
  <div class="pillar" style="background:var(--yellow);color:var(--yellow)">
    <div class="icon"><i role="img" aria-label="Stack of books icon" style="background:#f4a261"></i></div>
    <h3>SMART START</h3><p>Our Smart Start program is all about the cognitive development of your child.</p><a>READ MORE</a>
  </div>
  <div class="pillar" style="background:var(--tomato);color:var(--tomato)">
    <div class="icon"><i role="img" aria-label="Paint palette icon" style="background:#f6c28b"></i></div>
    <h3>INSPIRED</h3><p>The Inspired element of our curriculum is all about promoting creativity</p><a>READ MORE</a>
  </div>
  <div class="pillar" style="background:var(--navy);color:var(--navy)">
    <div class="icon"><i role="img" aria-label="Hands forming a heart icon" style="background:#ffc83d"></i></div>
    <h3>UNITE</h3><p>Our Unite element teaches children to be socially responsible, learn</p><a>READ MORE</a>
  </div>
  <div class="pillar" style="background:var(--blue);color:var(--blue)">
    <div class="icon"><i role="img" aria-label="Heart with heartbeat icon" style="background:#e8363b"></i></div>
    <h3>FIT</h3><p>Our Fit element promotes and educates the children about their physical well</p><a>READ MORE</a>
  </div>
  <div class="pillar" style="background:var(--green);color:var(--green)">
    <div class="icon"><i role="img" aria-label="Circle of people icon" style="background:#f7d04a"></i></div>
    <h3>CREW</h3><p>Our crew are professional, passionate, warm and love their jobs.</p><a>READ MORE</a>
  </div>
</section>

<section>
  <h2 class="abs hand section-title" style="top:1578px;color:var(--blue)">Our <span style="color:var(--orange)">Gallery</span></h2>
  <div class="abs gallery">
    <div role="img" aria-label="Colourful Tumble STEM hub interior" style="background:linear-gradient(135deg,#1d2a6b,#c9773a 70%,#e6b23c)"></div>
    <div role="img" aria-label="Educator and child exploring a plasma ball" style="background:linear-gradient(135deg,#2a2f8a,#6b5cc8 60%,#a9b6f0)"></div>
    <div role="img" aria-label="Children in lab coats at a sand table" style="background:linear-gradient(135deg,#2a3040,#8a8f9a 55%,#c99a62)"></div>
    <div role="img" aria-label="Children in the experiment lab" style="background:linear-gradient(135deg,#3a5a9a,#c7d6ee 55%,#e9ecf3)"></div>
    <div role="img" aria-label="Bright classroom with fireplace" style="background:linear-gradient(135deg,#e8e2d6,#b88b64 60%,#6d8fbf)"></div>
    <div role="img" aria-label="Outdoor play garden with shade sail" style="background:linear-gradient(135deg,#3f6b2c,#9cb86b 50%,#d1a25f)"></div>
  </div>
  <div class="btn btn-red" style="left:511px;top:2187px;width:177px;height:61px">Load More</div>
</section>

<section class="abs team">
  <div class="team-photo" role="img" aria-label="Educators with a toddler in a classroom"></div>
  <div class="team-card">
    <h2 class="hand">Join Our Team</h2>
    <p>When you join our team, you'll not only enjoy working in a flexible and supportive environment with many women in leadership positions, but you'll also gain skills and qualifications that will help your career thrive.</p>
    <div class="btn btn-red" style="left:47px;top:228px;width:162px;height:57px">Careers</div>
  </div>
</section>

<section>
  <h2 class="abs hand section-title" style="top:2858px;color:var(--blue)">Partnerships</h2>
  <div class="abs arrow" style="left:69px"><svg width="14" height="20" viewBox="0 0 14 20"><path d="M11 2 3 10l8 8" fill="none" stroke="#555" stroke-width="2.5"/></svg></div>
  <div class="abs partner" style="left:145px"><svg width="70" height="50"><rect x="5" y="5" width="60" height="40" rx="6" fill="#e9e9e9"/></svg></div>
  <div class="abs partner" style="left:378px"><svg width="70" height="50"><rect x="5" y="5" width="60" height="40" rx="6" fill="#e9e9e9"/></svg></div>
  <div class="abs partner active" style="left:612px"><svg width="70" height="50"><circle cx="35" cy="25" r="20" fill="#c9e6f2"/></svg></div>
  <div class="abs partner" style="left:845px"><svg width="70" height="50"><circle cx="35" cy="25" r="20" fill="#e9e9e9"/></svg></div>
  <div class="abs arrow" style="left:1087px"><svg width="14" height="20" viewBox="0 0 14 20"><path d="M3 2l8 8-8 8" fill="none" stroke="#555" stroke-width="2.5"/></svg></div>
</section>

<section class="abs tour">
  <h2 class="hand">Request A Tour</h2>
  <p>If you would like to tour one of our centres and meet<br>our friendly crew, please click the button below:</p>
  <div class="btn btn-yellow" style="left:605px;top:69px;width:289px;height:53px;font-size:15px">View Curriculum Handbook</div>
  <div class="btn btn-red" style="left:903px;top:69px;width:151px;height:53px;font-size:15px">Learn More</div>
</section>

<footer>
  <div class="abs foot-brand">Bright Sky<br>Kinder&shy;garten</div>
  <ul class="foot-nav">
    <li style="left:162px">Home</li>
    <li style="left:244px">About Us</li>
    <li style="left:341px">Gallery</li>
    <li style="left:645px">Sky Advantage™</li>
    <li style="left:813px">Locations</li>
    <li style="left:918px">Request A Tour</li>
  </ul>
  <div class="abs contact" style="left:261px">
    <div class="circ" style="background:#ffe600"><svg width="22" height="22" viewBox="0 0 22 22"><path d="M11 2a6 6 0 0 1 6 6c0 5-6 12-6 12S5 13 5 8a6 6 0 0 1 6-6z" fill="#1f6fc0"/><circle cx="11" cy="8" r="2.3" fill="#ffe600"/></svg></div>
    <div>Suite 4, 88 Harbour Road,<br>Kelvin Park 2200</div>
  </div>
  <div class="abs contact" style="left:645px">
    <div class="circ" style="background:var(--tomato)"><svg width="20" height="20" viewBox="0 0 32 32"><path d="M8 4c1.5-1.5 3-1.5 4 0l2 3.5c.7 1.3 0 2.4-.8 3l-1.3 1c1 2.7 3.2 4.9 5.9 5.9l1-1.3c.7-.8 1.8-1.5 3-.8L25.3 17c1.5 1 1.5 2.5 0 4-2 2-4.7 2.2-7.4.8-4-2-7.4-5.4-9.4-9.4C7.1 9.7 6 6 8 4z" fill="#fff"/></svg></div>
    <div>T: (02) 9000 1234 for NSW<br>or (07) 5000 0456 for QLD</div>
  </div>
  <p class="abs copy">© 2022 Bright Sky Kindergarten™ .All Rights Reserved &nbsp;|&nbsp; Sitemap &nbsp;|&nbsp; Privacy Policy &nbsp;|&nbsp; Contact</p>
  <div class="social"><span style="left:521px"></span><span style="left:565px"></span><span style="left:609px"></span><span style="left:653px"></span></div>
  <div class="abs grass" role="img" aria-label="Green grassy hills decoration"></div>
</footer>

</body>
</html>
```